Im open to ideas.. I was thinking on my business cards aswell as my logo. a place for my name. email. phone number and abn..

ive attched a file with my business logo. which i dont love the colours.. i was think a dark background with charcoal letters so something along those colour schumes but im open to ideas..

Business

BRL Constructions

```html
<!DOCTYPE html>
<html lang="en">
<head>
<meta charset="utf-8">
<title>BRL Constructions – Business Cards</title>
<link rel="stylesheet" href="https://fonts.googleapis.com/css2?family=Open+Sans:wght@400;600;700&display=swap">
<style>
  :root {
    --backdrop: #7a4d2e;
    --card-white: #ffffff;
    --charcoal: #231f20;
    --ink-soft: #4a4a4a;
    --accent-red: #e5202e;
  }
  * { margin: 0; padding: 0; box-sizing: border-box; }
  html, body {
    width: 1200px;
    height: 987px;
    overflow: hidden;
  }
  body {
    background: var(--backdrop);
    font-family: "Open Sans", Arial, sans-serif;
    position: relative;
  }
  .card {
    position: absolute;
    left: 306px;
    width: 615px;
    height: 352px;
    box-shadow: 0 3px 8px rgba(0, 0, 0, 0.35);
  }
  .card--front { top: 130px; background: var(--card-white); }
  .card--back { top: 505px; background: var(--charcoal); }

  .name-band {
    position: absolute;
    left: 0;
    top: 0;
    width: 615px;
    height: 120px;
  }
  .holder-name {
    position: absolute;
    left: 41px;
    top: 46px;
    color: #fff;
    font-size: 21px;
    font-weight: 600;
    line-height: 1;
  }
  .holder-title {
    position: absolute;
    left: 41px;
    top: 75px;
    color: #fff;
    font-size: 16px;
    font-weight: 400;
    line-height: 1;
  }

  .brand {
    position: absolute;
    display: flex;
    align-items: center;
    gap: 12px;
    font-weight: 700;
    text-transform: uppercase;
    white-space: nowrap;
    line-height: 1;
  }
  .brand__mark {
    width: 18px;
    height: 18px;
    background: var(--accent-red);
    flex: none;
  }
  .card--front .brand {
    right: 42px;
    top: 96px;
    color: var(--charcoal);
    font-size: 30px;
    letter-spacing: 1px;
  }
  .card--back .brand {
    left: 0;
    right: 0;
    top: 150px;
    justify-content: center;
    color: #fff;
    font-size: 44px;
    letter-spacing: 2px;
  }
  .card--back .brand__mark { width: 26px; height: 26px; }

  .contact {
    position: absolute;
    left: 41px;
    top: 270px;
    list-style: none;
    color: var(--ink-soft);
    font-size: 16px;
  }
  .contact li {
    display: flex;
    align-items: center;
    gap: 12px;
    height: 24px;
  }
  .contact svg { width: 17px; height: 17px; fill: var(--accent-red); }

  .company-info {
    position: absolute;
    right: 34px;
    top: 270px;
    text-align: right;
    font-size: 16px;
    letter-spacing: 0.5px;
  }
  .company-info p { height: 24px; line-height: 24px; }
  .abn { color: var(--ink-soft); }
  .web { color: var(--accent-red); letter-spacing: 1px; }
</style>
</head>
<body>
  <section class="card card--front" aria-label="Business card front">
    <svg class="name-band" viewBox="0 0 615 120" aria-hidden="true">
      <polygon points="0,35 377,35 292,96 0,103" fill="#231f20"/>
    </svg>
    <p class="holder-name">Sam Keller</p>
    <p class="holder-title">President</p>

    <div class="brand"><span class="brand__mark"></span>BRL Constructions</div>

    <ul class="contact">
      <li>
        <svg viewBox="0 0 24 24" aria-hidden="true"><path d="M3 6c0-2 4-3 9-3s9 1 9 3v2h-4V6.5c-1-.5-3-.8-5-.8s-4 .3-5 .8V8H3zM6 10h12l2 9H4zm6 2.5a3 3 0 1 0 0 6 3 3 0 0 0 0-6z"/></svg>
        555 0142 7788
      </li>
      <li>
        <svg viewBox="0 0 24 24" aria-hidden="true"><path d="M2 6h20v1l-10 6L2 7zm0 3l10 6 10-6v9H2z"/></svg>
        sam@brlmail.com
      </li>
    </ul>

    <div class="company-info">
      <p class="abn">ABN: 123456789</p>
      <p class="web">www.brlbuilds.com</p>
    </div>
  </section>

  <section class="card card--back" aria-label="Business card back">
    <div class="brand"><span class="brand__mark"></span>BRL Constructions</div>
  </section>
</body>
</html>
```